Business card and stationary for consulting business

We need business cards and matching stationary for professional consulting business for employment and human resources issues.
One of the CraftHive designers designed the logo with our company name.  Use the colors in the logo and may use light yellow as an accent color.
Add
Mara T. Vollen, J.D., LL.M.
485 E. Callister Lane
Winter Park, Florida  32789
407-555-0183
maravollenjd@quillpost.example

Industry/Entity Type
Business

```html
<!DOCTYPE html>
<html lang="en">
<head>
<meta charset="utf-8">
<title>Stridewell Business Card</title>
<link rel="stylesheet" href="https://fonts.googleapis.com/css2?family=Quicksand:wght@400;500;600&display=swap">
<style>
  :root {
    --bg: #eceff1;
    --panel-blue: #1f78a4;
    --sky: #4dd2f8;
    --brand-blue: #2a86b5;
    --tag-cyan: #3cc4ee;
    --white: #ffffff;
    --rule: #c9d3d8;
    --print: #1d6f99;
  }
  * { box-sizing: border-box; margin: 0; padding: 0; }
  html, body {
    width: 1200px; height: 900px; overflow: hidden;
    background: var(--bg);
    font-family: "Quicksand", sans-serif;
  }
  .sheet {
    width: 1200px; height: 900px;
    display: flex; flex-direction: column;
    align-items: center; justify-content: center; gap: 50px;
  }
  .card {
    position: relative;
    width: 665px; height: 380px;
    background: var(--white);
    box-shadow: 0 6px 20px rgba(0,0,0,0.12);
    overflow: hidden;
  }
  /* Front */
  .card-front .contact-panel {
    position: absolute; left: 0; top: 0;
    width: 300px; height: 100%;
    background: var(--panel-blue);
    color: var(--white);
    padding: 40px 0 0 28px;
  }
  .holder-name {
    font-weight: 400; font-size: 23px; line-height: 1.2;
    white-space: nowrap;
  }
  .holder-name .surname { display: block; padding-left: 12px; }
  .contact-list { list-style: none; margin-top: 52px; font-size: 12px; }
  .contact-list li {
    display: flex; align-items: flex-start; gap: 14px;
    margin-bottom: 20px; line-height: 1.5; white-space: nowrap;
  }
  .contact-list svg { flex: none; width: 14px; height: 14px; margin-top: 2px; }
  .brand-block {
    position: absolute; display: flex; align-items: flex-start;
  }
  .card-front .brand-block { left: 322px; top: 80px; }
  .brand-name {
    font-weight: 500; font-size: 34px; color: var(--brand-blue);
    line-height: 1; padding-right: 12px; margin-top: 8px;
  }
  .tagline {
    border-left: 1px solid var(--rule);
    padding-left: 10px; padding-top: 18px;
    font-size: 13px; line-height: 1.2; color: var(--tag-cyan);
    white-space: nowrap;
  }
  .footsteps {
    position: absolute; left: 318px; top: 292px;
    width: 170px; height: 62px;
    background: linear-gradient(100deg, rgba(29,111,153,0.18), rgba(29,111,153,0.38));
    border-radius: 4px;
  }
  /* Back */
  .card-back .sky-wedge { position: absolute; inset: 0; width: 100%; height: 100%; }
  .card-back .brand-block { right: 40px; bottom: 70px; }
</style>
</head>
<body>
<main class="sheet">
  <section class="card card-front">
    <div class="contact-panel">
      <h1 class="holder-name">Mara<span class="surname">T. Vollen, J.D., LL.M.</span></h1>
      <ul class="contact-list">
        <li>
          <svg viewBox="0 0 14 14"><rect x="3.5" y="0.5" width="7" height="13" rx="1.2" fill="none" stroke="#fff"/><line x1="6" y1="11.5" x2="8" y2="11.5" stroke="#fff"/></svg>
          <span>407-555-0183</span>
        </li>
        <li>
          <svg viewBox="0 0 14 14"><path d="M7 0.5a4.5 4.5 0 0 0-4.5 4.5c0 3.2 4.5 8.5 4.5 8.5s4.5-5.3 4.5-8.5A4.5 4.5 0 0 0 7 0.5z" fill="#fff"/><circle cx="7" cy="5" r="1.6" fill="#1f78a4"/></svg>
          <span>485 E. Callister Lane<br>Harlow Springs, Florida 32899</span>
        </li>
        <li>
          <svg viewBox="0 0 14 14"><rect x="0.5" y="2.5" width="13" height="9" fill="#fff"/><polyline points="0.5,2.5 7,8 13.5,2.5" fill="none" stroke="#1f78a4"/></svg>
          <span>maravollenjd@quillpost.example</span>
        </li>
      </ul>
    </div>
    <div class="brand-block">
      <div class="brand-name">Stridewell</div>
      <div class="tagline">Grow Income<br>Control Costs<br>Secure Margins</div>
    </div>
    <div class="footsteps" role="img" aria-label="Trail of small footprints walking toward the right"></div>
  </section>

  <section class="card card-back">
    <svg class="sky-wedge" viewBox="0 0 665 380" preserveAspectRatio="none">
      <polygon points="0,0 665,0 665,95 0,185" fill="#4dd2f8"/>
    </svg>
    <div class="brand-block">
      <div class="brand-name">Stridewell</div>
      <div class="tagline">Grow Income<br>Control Costs<br>Secure Margins</div>
    </div>
  </section>
</main>
</body>
</html>
```